Stationary for Keeping Steady

we are in the process of creating a more professional image for our company Keeping Steady Paramedical Services. We have recently had a new logo and general brochure designed using artpitchhub and have been impressed by the quality of submissions.

We need:
- Letterhead (A4)
- Business Cards
- With compliments slips
- Email stationary

Letterhead information:
Address - 47 Wattlebrook Drive, Fernhollow Vic 3091
Phone - 1800 462 817
email - enquiries@keepsteady.com.au
Internet - www.keepsteady.com.au
ABN - 82 463 915 207
ACN - 264 871 035

Files need to be able to be edited in Illustrator CS2

Business Cards / with compliments slips / email stationary:
Double sided.
One side to have Name, Mobile number, company phone 1800462817, email, internet address

Files need to be able to be edited in Illustrator CS2 (except email stationary)

Our website is www.keepsteady.com.au for more information. Do not base designs on the website as it will eventually be revised.

Target Market(s)

Australian based businesses, government departments and schools. We specialise in corporate customers rather than public first aid course

Industry/Entity Type

Internet

Requirements
Must have
• Where applicable file to be editable in illustrator CS2 to allow future alterations.

```html
<!DOCTYPE html>
<html lang="en">
<head>
<meta charset="utf-8">
<title>Keeping Steady Paramedical Services – Stationery</title>
<link href="https://fonts.googleapis.com/css2?family=Questrial&family=Open+Sans:wght@400;700&display=swap" rel="stylesheet">
<style>
  :root {
    --red: #c8232c;
    --red-dark: #8e1418;
    --black: #111111;
    --paper: #ffffff;
    --backdrop: #e7e4e0;
    --ink: #222222;
    --muted: #555555;
  }
  * { box-sizing: border-box; margin: 0; padding: 0; }
  html, body { width: 1200px; height: 900px; overflow: hidden; }
  body {
    position: relative;
    background: var(--backdrop);
    font-family: "Open Sans", Arial, sans-serif;
    color: var(--ink);
  }
  .sheet {
    position: absolute;
    background: var(--paper);
    box-shadow: 0 2px 6px rgba(0,0,0,.18);
    overflow: hidden;
  }
  .side-band {
    position: absolute; left: 0; top: 0; bottom: 0;
    background: linear-gradient(90deg, var(--red-dark), var(--red) 60%, var(--red-dark));
  }
  .side-band::after {
    content: ""; position: absolute; left: 0; right: 0; bottom: 0; height: 9%;
    background: var(--black);
  }
  .brand { position: absolute; display: flex; align-items: flex-start; gap: 8px; color: var(--red); font-family: "Questrial", Arial, sans-serif; }
  .brand-square { background: var(--red); flex: none; }
  .brand-name { line-height: 1; }
  .brand-name span { display: block; }
  .brand-name .sub { margin-top: 2px; }

  /* Letterhead */
  .letterhead { left: 26px; top: 55px; width: 560px; height: 790px; }
  .letterhead .side-band { width: 27px; }
  .letterhead .brand { left: 48px; top: 26px; }
  .letterhead .brand-square { width: 26px; height: 26px; }
  .letterhead .brand-name .main { font-size: 20px; }
  .letterhead .brand-name .sub { font-size: 10px; }

  .contact-row {
    position: absolute; display: flex; font-size: 9px; line-height: 1.35; color: var(--ink);
  }
  .contact-row .col { padding: 0 14px; border-left: 1px solid var(--red); }
  .contact-row .col:first-child { border-left: none; padding-left: 0; }
  .letterhead .contact-row { left: 50px; bottom: 22px; }

  /* Business cards */
  .card { top: 75px; width: 226px; height: 146px; border-radius: 9px; }
  .card-front { left: 660px; }
  .card-front .side-band { width: 16px; }
  .card-front .brand { right: 14px; top: 12px; gap: 5px; }
  .card-front .brand-square { width: 14px; height: 14px; }
  .card-front .brand-name .main { font-size: 12px; }
  .card-front .brand-name .sub { font-size: 6px; }
  .card-details { position: absolute; left: 26px; top: 72px; font-size: 5.2px; line-height: 1.35; color: var(--muted); }
  .card-details .person { font-size: 8.5px; font-weight: 700; color: var(--black); margin-bottom: 5px; }
  .card-details .gap { height: 5px; }

  .card-back { left: 918px; }
  .card-back .accent { position: absolute; left: 0; top: 0; width: 84px; height: 146px; background: linear-gradient(135deg, #e0323a, var(--red-dark)); }
  .card-back .band { position: absolute; left: 84px; right: 0; top: 56px; height: 44px; background: var(--black); }
  .card-back .brand { right: 14px; top: 62px; }
  .card-back .brand-name { text-align: right; }
  .card-back .brand-name .main { font-size: 15px; }
  .card-back .brand-name .sub { font-size: 7.5px; }

  /* Compliments slip */
  .comp-slip { left: 620px; top: 245px; width: 560px; height: 265px; }
  .comp-slip .side-band { width: 23px; }
  .comp-slip .brand { left: 38px; top: 22px; }
  .comp-slip .brand-square { width: 26px; height: 26px; }
  .comp-slip .brand-name .main { font-size: 20px; }
  .comp-slip .brand-name .sub { font-size: 10px; }
  .comp-title { position: absolute; left: 265px; top: 30px; font-family: "Questrial", Arial, sans-serif; font-size: 16px; color: var(--black); }
  .comp-slip .contact-row { left: 52px; bottom: 18px; }

  /* Email stationery */
  .email { left: 620px; top: 540px; width: 560px; height: 262px; }
  .email .accent { position: absolute; left: 0; top: 0; width: 180px; height: 180px; background: linear-gradient(135deg, #e0323a, var(--red-dark)); }
  .email .band { position: absolute; left: 180px; right: 0; top: 85px; height: 80px; background: var(--black); }
  .email .brand { right: 48px; top: 102px; }
  .email .brand-name { text-align: right; }
  .email .brand-name .main { font-size: 30px; }
  .email .brand-name .sub { font-size: 15px; margin-top: 4px; }
  .email-web { position: absolute; right: 68px; bottom: 12px; font-size: 11px; letter-spacing: 2px; color: var(--black); }
</style>
</head>
<body>

<section class="sheet letterhead" aria-label="Letterhead">
  <div class="side-band"></div>
  <div class="brand">
    <div class="brand-square"></div>
    <div class="brand-name"><span class="main">Keeping Steady</span><span class="sub">Paramedical Services Pty Ltd</span></div>
  </div>
  <div class="contact-row">
    <div class="col">47 Wattlebrook Drive,<br>Fernhollow Vic 3091</div>
    <div class="col">P : 1800 462 817<br>F : 1800 356 201</div>
    <div class="col">E : enquiries@keepsteady.com.au<br>W : www.keepsteady.com.au</div>
    <div class="col">ABN - 82 463 915 207<br>ACN - 264 871 035</div>
  </div>
</section>

<section class="sheet card card-front" aria-label="Business card front">
  <div class="side-band"></div>
  <div class="brand">
    <div class="brand-square"></div>
    <div class="brand-name"><span class="main">Keeping Steady</span><span class="sub">Paramedical Services Pty Ltd</span></div>
  </div>
  <div class="card-details">
    <div class="person">Jordan Lee</div>
    47 Wattlebrook Drive,<br>Fernhollow Vic 3091<br>
    T 1800 462 817<br>M 0412 345 678<br>enquiries@keepsteady.com.au
    <div class="gap"></div>
    ABN - 82 463 915 207<br>ACN - 264 871 035
  </div>
</section>

<section class="sheet card card-back" aria-label="Business card back">
  <div class="accent"></div>
  <div class="band"></div>
  <div class="brand">
    <div class="brand-name"><span class="main">Keeping Steady</span><span class="sub">Paramedical Services Pty Ltd</span></div>
  </div>
</section>

<section class="sheet comp-slip" aria-label="With compliments slip">
  <div class="side-band"></div>
  <div class="brand">
    <div class="brand-square"></div>
    <div class="brand-name"><span class="main">Keeping Steady</span><span class="sub">Paramedical Services Pty Ltd</span></div>
  </div>
  <div class="comp-title">With Compliment</div>
  <div class="contact-row">
    <div class="col">47 Wattlebrook Drive,<br>Fernhollow Vic 3091</div>
    <div class="col">P : 1800 462 817<br>F : 1800 356 201</div>
    <div class="col">E : enquiries@keepsteady.com.au<br>W : www.keepsteady.com.au</div>
    <div class="col">ABN - 82 463 915 207<br>ACN - 264 871 035</div>
  </div>
</section>

<section class="sheet email" aria-label="Email stationery">
  <div class="accent"></div>
  <div class="band"></div>
  <div class="brand">
    <div class="brand-name"><span class="main">Keeping Steady</span><span class="sub">Paramedical Services Pty Ltd</span></div>
  </div>
  <div class="email-web">www.keepsteady.com.au</div>
</section>

</body>
</html>
```